Solo consultant in research/analytics/data science space needs new business card

I need a new business card to promote my solo business as creative problem solver and consultant. I work on business projects for sales and market research and analytics, customer/market insights, and data science. I provide clients data-informed insights and ideas to enhance their businesses. My initial tagline: 'Make your data work for YOU.'

People should hire me because of my diverse background. Because of my Ph.D. in Political Science I have a strong background in research and analytics, project design and management, and communications skills. With my experience as a marketing analyst, a volunteer on non-profit projects, and currently as research consultant I have worked on projects within various industries. I also have a taste for improvisation so I enjoy thinking creatively and appreciate design thinking.

As an introduction to my background: Clients might want to hire me for many types of projects. Clients might wish to understand who their best customers are and how to characterize them. Maybe clients want to know how their customers feel about a certain product or service. Clients might want to know more about their local market area and overall industry. Clients might want to know whether their marketing programs are effective or else what drives their sales revenue. Perhaps clients want to use their data to create something useful for themselves or their customers.

One client hired me to help them decide whether to expand their services to newer customers. I gathered and analyzed information about the local area – the characteristics of people living there as well as the client’s competitors – and described trends and implications. The client was very pleased with the results and submitted them to superiors for approval to move forward.

For another client – who was looking to purchase a house in a metropolitan area – I gathered population and school data about the area. With this, I created an interactive mapping tool so they could zoom in on neighborhoods and learn more about them before they selected a neighborhood to purchase a house. They were happy with the results of my work.

When I worked as a marketing analyst for a consulting firm, a Vice President of Marketing hired us to discover whether or not the company’s marketing programs (i.e. coupons and discounts) were effective. I analyzed their data and our team discovered their marketing was indeed effective. He was very happy and used this to justify their programs to the Finance department (who thought such programs lost revenue).

- Marcus Delano Whitby, Ph.D.

Target Market(s)

Future clients and employers. The most immediate target markets will be other service providers such as consulting companies, marketing firms and ad agencies. I will also use this for meeting with clients in various industries.

Industry/Entity Type

Consulting

Contact Information for Business Card

Since it is my first real business card as a solo practitioner, I want to make an excellent first impression. I want this useful in case someone hires me to work on projects or else hire me to work within a firm or company. The card should convey competence and some creativity while also being neither stuffy nor a data geek.

Colors

Designer to choose colors to be used in the design.

Requirements
Nice to have
• Attached are the starting efforts at the card to add some color. It will be nice to use my name and descriptors on one side and tagline on the other. If anyone has better ideas, I will love to see them!

```html
<!DOCTYPE html>
<html lang="en">
<head>
<meta charset="UTF-8">
<title>Marcus Delano Whitby, Ph.D. – Business Card</title>
<link href="https://fonts.googleapis.com/css2?family=Montserrat:wght@500;600;700&family=Lato:wght@400;700&display=swap" rel="stylesheet">
<style>
  :root {
    --bg: #2b2b2b;
    --card: #1d1d1d;
    --band: #ffffff;
    --red: #e0262b;
    --ink-light: #f4f4f4;
    --ink-grey: #6f6f6f;
    --rule: #cfcfcf;
  }
  * { margin: 0; padding: 0; box-sizing: border-box; }
  html, body { width: 1200px; height: 895px; overflow: hidden; background: var(--bg); }
  .canvas {
    width: 1200px; height: 895px;
    display: flex; flex-direction: column; align-items: center; justify-content: center; gap: 30px;
  }
  .card {
    position: relative; width: 700px; height: 400px;
    background: var(--card); overflow: hidden;
    box-shadow: 0 10px 30px rgba(0,0,0,.45);
  }

  /* Front: tagline */
  .tagline {
    position: absolute; left: 0; right: 0; top: 150px; text-align: center;
    font-family: 'Montserrat', sans-serif; font-weight: 700; font-size: 38px;
    color: var(--ink-light); letter-spacing: .5px;
  }
  .front-web {
    position: absolute; left: 0; right: 0; top: 240px; text-align: center;
    font-family: 'Lato', sans-serif; font-size: 15px; color: var(--ink-light); letter-spacing: .3px;
  }
  .front-web .accent { color: var(--red); }

  /* Back: identity */
  .name-band {
    position: absolute; left: 0; top: 70px; width: 100%; height: 140px; background: var(--band);
  }
  .name {
    position: absolute; left: 46px; top: 40px;
    font-family: 'Montserrat', sans-serif; font-weight: 600; font-size: 38px;
    color: var(--red); text-transform: uppercase; letter-spacing: -.5px; white-space: nowrap;
  }
  .name .degree { text-transform: none; }
  .descriptors {
    position: absolute; left: 48px; top: 86px;
    font-family: 'Lato', sans-serif; font-size: 15.5px; color: var(--ink-grey); letter-spacing: 1px;
  }
  .role-tab {
    position: absolute; right: 0; top: 190px; width: 230px; height: 52px;
  }
  .role-tab span {
    position: absolute; left: 0; right: 0; top: 24px; text-align: center;
    font-family: 'Montserrat', sans-serif; font-weight: 600; font-size: 16px; color: #fff; letter-spacing: 1px;
  }
  .location {
    position: absolute; right: 48px; top: 268px; display: flex; align-items: center; gap: 12px;
    font-family: 'Lato', sans-serif; font-size: 16px; color: var(--ink-light); letter-spacing: .5px;
  }
  .contacts {
    position: absolute; left: 110px; top: 262px; padding-left: 28px;
    border-left: 1px solid var(--rule); list-style: none;
  }
  .contacts li {
    display: flex; align-items: center; gap: 12px; height: 27px;
    font-family: 'Lato', sans-serif; font-size: 16px; color: var(--ink-light); letter-spacing: .3px;
  }
  .contacts svg { width: 16px; height: 16px; flex: none; }
</style>
</head>
<body>
<main class="canvas">

  <section class="card card-front" aria-label="Card front">
    <p class="tagline">Make Your data work for YOU.</p>
    <p class="front-web">www.<span class="accent">marcusdelanowhitby</span>.com</p>
  </section>

  <section class="card card-back" aria-label="Card back">
    <div class="name-band">
      <h1 class="name">Marcus Delano Whitby, <span class="degree">Ph.D.</span></h1>
      <p class="descriptors">Research/Analytics - Customer Intelligence - Data Science</p>
    </div>

    <div class="role-tab">
      <svg width="230" height="52" viewBox="0 0 230 52" aria-hidden="true">
        <path d="M14 20 H230 V52 H22 Q14 52 14 44 Z" fill="var(--red)"/>
        <path d="M0 20 L14 0 H230 V20 Z" fill="var(--red)"/>
      </svg>
      <span>Consultant</span>
    </div>

    <div class="location">
      <svg width="16" height="20" viewBox="0 0 16 20" aria-hidden="true">
        <path d="M8 1 C4 1 1.5 4 1.5 7.5 C1.5 12 8 19 8 19 C8 19 14.5 12 14.5 7.5 C14.5 4 12 1 8 1 Z" fill="none" stroke="var(--red)" stroke-width="1.6"/>
        <circle cx="8" cy="7.5" r="2.4" fill="none" stroke="var(--red)" stroke-width="1.4"/>
      </svg>
      Lisbon, PT
    </div>

    <ul class="contacts">
      <li>
        <svg viewBox="0 0 16 16" aria-hidden="true"><rect x="4" y="1" width="8" height="14" rx="1.5" fill="none" stroke="var(--red)" stroke-width="1.5"/><circle cx="8" cy="12.5" r=".9" fill="var(--red)"/></svg>
        +351 912 340 586
      </li>
      <li>
        <svg viewBox="0 0 16 16" aria-hidden="true"><rect x="1" y="3.5" width="14" height="9.5" fill="var(--red)"/><path d="M1 3.5 L8 9 L15 3.5" fill="none" stroke="var(--card)" stroke-width="1.3"/></svg>
        mdwhitby70@inboxpost.com
      </li>
      <li>
        <svg viewBox="0 0 16 16" aria-hidden="true"><circle cx="8" cy="8" r="6.5" fill="none" stroke="var(--red)" stroke-width="1.4"/><ellipse cx="8" cy="8" rx="3" ry="6.5" fill="none" stroke="var(--red)" stroke-width="1.2"/><path d="M1.5 8 H14.5" stroke="var(--red)" stroke-width="1.2"/></svg>
        www.marcusdelanowhitby.com
      </li>
      <li>
        <svg viewBox="0 0 16 16" aria-hidden="true"><circle cx="8" cy="8" r="6" fill="var(--red)"/></svg>
        @MarcusWhitby70
      </li>
    </ul>
  </section>

</main>
</body>
</html>
```